DL Flyer Design

I need a DL flyer, double-sided designed for a Brisbane based outdoor group exercise/training company called Move Ahead! Move Ahead! provides group outdoor training, designed for the individual. It provides the support, motivation and one-on-one attention of personal training combined with the support of a group environment. The classes are fun, challenging and aim to develop confidence & fitness. Weight loss is not the focus, although it is a benefit.
Updates

Hi

I've just uploaded a high res version of the logo if you need.

Cheers
Tam

Target Market(s)

English speaking men & women aged 25 - 45, white-collar office jobs. Average-low level of fitness, not hugely 'fitness' oriented but want to improve quality of life, overall fitness, lose a bit of weight.

Computer and consumer literate. Live in suburban Brisbane, Australia.

Industry/Entity Type

Training

Requirements
Must have
• Double sided DL. Use of black, greens and white per attached photos. Use of 1300 572 914 (1300 RUN FAR) and website www.movaheadactive.com.au

Indicative copy and contents is posted in the comments section.

```html
<!DOCTYPE html>
<html lang="en">
<head>
<meta charset="utf-8">
<title>Move Ahead! – DL Flyer</title>
<link rel="stylesheet" href="https://fonts.googleapis.com/css2?family=Source+Sans+3:wght@600;700&family=Arimo:wght@400;700&display=swap">
<style>
  :root {
    --green: #3dae3a;
    --green-light: #8cc63f;
    --green-wash: #cfe8b4;
    --blue: #5ab7e0;
    --black: #1d1b1a;
    --white: #ffffff;
    --ink: #231f20;
  }
  * { margin: 0; padding: 0; box-sizing: border-box; }
  html, body { width: 1200px; height: 2404px; overflow: hidden; background: var(--white); }
  .flyer {
    position: relative;
    width: 1200px;
    height: 2404px;
    overflow: hidden;
    background: var(--white);
    font-family: "Arimo", Arial, sans-serif;
    color: var(--ink);
  }
  .hero-figure {
    position: absolute;
    left: 0; top: 0;
    width: 1200px; height: 2250px;
    background:
      radial-gradient(ellipse 420px 900px at 560px 820px, rgba(140,198,63,0.28), rgba(140,198,63,0) 70%),
      radial-gradient(ellipse 380px 260px at 820px 260px, rgba(140,198,63,0.22), rgba(140,198,63,0) 70%),
      radial-gradient(ellipse 300px 200px at 250px 330px, rgba(140,198,63,0.2), rgba(140,198,63,0) 70%);
  }
  .deco { position: absolute; left: 0; top: 0; }
  .content { position: absolute; left: 0; top: 0; width: 1200px; }
  .section-title {
    position: absolute;
    left: 127px;
    font-family: "Source Sans 3", "Myriad Pro", sans-serif;
    font-weight: 700;
    font-size: 54px;
    color: var(--green);
    line-height: 1;
  }
  .sub-title {
    position: absolute;
    left: 193px;
    font-family: "Source Sans 3", "Myriad Pro", sans-serif;
    font-weight: 700;
    font-size: 56px;
    color: var(--ink);
    line-height: 1;
  }
  .body-text {
    position: absolute;
    left: 127px;
    width: 1010px;
    font-size: 33px;
    line-height: 1.3;
  }
  .list { position: absolute; list-style: none; font-size: 33px; line-height: 1.3; }
  .list li { position: relative; padding-left: 58px; margin-bottom: 9px; }
  .list li::before {
    content: "\00BB";
    position: absolute; left: 0; top: -2px;
    font-weight: 700; color: var(--ink);
  }
  .benefits { left: 154px; top: 928px; width: 960px; }
  .messages { left: 243px; top: 1244px; width: 880px; }
  .key-title { left: 0; width: 1240px; text-align: center; }
  .swoosh { position: absolute; left: 0; top: 1500px; }
  .brand {
    position: absolute;
    left: 720px; top: 1640px;
    display: flex; align-items: center; gap: 22px;
    font-family: "Source Sans 3", "Myriad Pro", sans-serif;
    font-weight: 700;
    font-size: 96px;
    color: var(--green);
    line-height: 1;
  }
  .brand-dot { width: 44px; height: 44px; border-radius: 50%; background: var(--black); }
  .contact { position: absolute; left: 46px; color: var(--white); font-family: "Arimo", Arial, sans-serif; font-weight: 700; line-height: 1; }
  .phone { top: 2064px; font-size: 86px; }
  .web { top: 2236px; font-size: 70px; font-weight: 400; }
</style>
</head>
<body>
<main class="flyer">
  <div class="hero-figure" role="img" aria-label="Faint green silhouette of a woman leaping with arms outstretched"></div>

  <svg class="deco" width="1200" height="700" viewBox="0 0 1200 700" aria-hidden="true">
    <path d="M0 330 C 160 220, 330 190, 520 200" fill="none" stroke="var(--green)" stroke-width="10"/>
    <path d="M0 370 C 180 260, 360 230, 560 236" fill="none" stroke="var(--green-light)" stroke-width="5"/>
    <path d="M0 250 C 120 180, 240 150, 380 150" fill="none" stroke="var(--blue)" stroke-width="6"/>
  </svg>

  <div class="content">
    <h2 class="section-title" style="top:468px;">Geographic Distribution</h2>
    <p class="body-text" style="top:562px;">Live within a 5km radius of chosen park location Woolloongabba/Stones Corner/Greenslopes</p>

    <h2 class="section-title" style="top:696px;">Benefits and Key Messages</h2>
    <h3 class="sub-title" style="top:770px;">Primary Benefits to the Consumer</h3>
    <p class="body-text" style="top:854px; left:46px;">The primary benefits to the consumer are:</p>
    <ul class="list benefits">
      <li>Personal attention and support to achieve your fitness goals</li>
      <li>Program structured to enable long-term commitment – a sustainable investment in your health</li>
    </ul>

    <h2 class="section-title key-title" style="top:1124px;">Key Messages</h2>
    <ul class="list messages">
      <li>Personalised training in a group environment;</li>
      <li>Designed for you, to meet your needs;</li>
      <li>Affordable price that works within your budget; and</li>
      <li>Flexible schedule that works within your lifestyle</li>
    </ul>
  </div>

  <svg class="swoosh" width="1200" height="904" viewBox="0 0 1200 904" aria-hidden="true">
    <path d="M0 280 C 300 120, 750 60, 1200 40 L1200 80 C 760 110, 320 190, 0 330 Z" fill="var(--blue)"/>
    <path d="M0 330 C 320 190, 760 110, 1200 80 L1200 110 C 760 150, 330 230, 0 360 Z" fill="var(--white)"/>
    <path d="M0 360 C 330 230, 760 150, 1200 110 L1200 150 C 800 190, 380 270, 0 400 Z" fill="var(--green-light)"/>
    <path d="M0 400 C 380 270, 800 190, 1200 150 L1200 904 L0 904 Z" fill="var(--black)"/>
  </svg>

  <div class="brand">
    <span class="brand-dot"></span>
    <span>Move Ahead!</span>
  </div>

  <p class="contact phone">1300 572 914</p>
  <p class="contact web">www.movaheadactive.com.au</p>
</main>
</body>
</html>
```